Car transport business

We need a new business card design. Attached is our old card sample. I would just like to adjust the logo colors (blue and red) to be brighter. I changed my name to the brighter red and the word dispatcher to a brighter blue as an example. But you can adjust those colors further. And then perhaps you can use the same colors for the card design but use your imagination.

As a suggestion so the card stands out I would like to add a clip art of car carrier truck. Attached are examples of that as well

```html
<!DOCTYPE html>
<html lang="en">
<head>
<meta charset="utf-8">
<title>Summit Haul – Business Card</title>
<link rel="stylesheet" href="https://fonts.googleapis.com/css2?family=Roboto:wght@400;500;900&display=swap">
<style>
  :root {
    --stage: #6e6e70;
    --card: #1f1e20;
    --card-deep: #181719;
    --emboss: #2a292c;
    --edge-red: #e3141b;
    --brand-red: #ff1a1a;
    --brand-blue: #1a7fe0;
    --ink-white: #f4f4f4;
  }
  * { box-sizing: border-box; margin: 0; padding: 0; }
  html, body { width: 1200px; height: 800px; overflow: hidden; }
  body {
    background: var(--stage);
    font-family: "Roboto", Arial, sans-serif;
    display: flex;
    align-items: center;
    justify-content: center;
    gap: 40px;
  }
  .card {
    position: relative;
    width: 540px;
    height: 309px;
    background: var(--card);
    border-radius: 18px;
    border-bottom: 2px solid var(--edge-red);
    border-right: 2px solid var(--edge-red);
    overflow: hidden;
  }

  /* Contact side */
  .card-contact .emboss-art {
    position: absolute;
    left: 40px; top: 30px;
    width: 270px; height: 260px;
    border-radius: 130px 130px 20px 20px;
    background: radial-gradient(ellipse at 50% 60%, var(--emboss), var(--card) 70%);
  }
  .contact-block {
    position: absolute;
    right: 34px; top: 50px;
    text-align: right;
  }
  .person-name {
    color: var(--brand-red);
    font-weight: 900;
    font-size: 30px;
    letter-spacing: 0.5px;
    line-height: 1;
  }
  .person-role {
    color: var(--brand-blue);
    font-weight: 500;
    font-size: 19px;
    margin-top: 4px;
    margin-bottom: 16px;
  }
  .contact-list { list-style: none; }
  .contact-item {
    display: flex;
    justify-content: flex-end;
    align-items: center;
    gap: 10px;
    color: var(--ink-white);
    font-size: 16px;
    line-height: 26px;
  }
  .contact-icon { width: 14px; height: 14px; flex: none; }

  /* Brand side */
  .card-brand .pattern-art {
    position: absolute; inset: 0;
    background: linear-gradient(160deg, #232225 0%, var(--card) 50%, var(--card-deep) 100%);
  }
  .brand-lockup {
    position: absolute;
    left: 50%; top: 50%;
    transform: translate(-50%, -50%);
    display: flex;
    align-items: center;
    gap: 14px;
  }
  .brand-dot {
    width: 46px; height: 46px;
    border-radius: 50%;
    background: var(--brand-blue);
    flex: none;
  }
  .brand-name {
    color: var(--brand-red);
    font-weight: 900;
    font-size: 44px;
    letter-spacing: 2px;
    line-height: 1;
  }
  .brand-tagline {
    color: var(--brand-blue);
    font-size: 11.5px;
    letter-spacing: 3.4px;
    text-transform: uppercase;
    margin-top: 6px;
  }
</style>
</head>
<body>

  <section class="card card-contact">
    <div class="emboss-art" role="img" aria-label="Blind-embossed outline of a car seen from the front with sweeping road curves"></div>
    <div class="contact-block">
      <h1 class="person-name">REED CALLOWAY</h1>
      <p class="person-role">Dispatcher</p>
      <ul class="contact-list">
        <li class="contact-item">555-201-0148
          <svg class="contact-icon" viewBox="0 0 16 16"><path d="M4 1l3 3-2 2c1 2 3 4 5 5l2-2 3 3-2 3C7 15 1 9 1 3z" fill="var(--brand-blue)"/></svg>
        </li>
        <li class="contact-item">555-201-0193
          <svg class="contact-icon" viewBox="0 0 16 16"><rect x="4" y="1" width="8" height="14" rx="1.5" fill="none" stroke="var(--brand-blue)" stroke-width="1.6"/><circle cx="8" cy="12.5" r="0.9" fill="var(--brand-blue)"/></svg>
        </li>
        <li class="contact-item">summithaulco@mail.com
          <svg class="contact-icon" viewBox="0 0 16 16"><rect x="1" y="3" width="14" height="10" rx="1" fill="var(--brand-blue)"/><path d="M1.5 4l6.5 5 6.5-5" fill="none" stroke="var(--card)" stroke-width="1.3"/></svg>
        </li>
        <li class="contact-item">www.summithaulco.com
          <svg class="contact-icon" viewBox="0 0 16 16"><circle cx="8" cy="8" r="6.5" fill="none" stroke="var(--brand-blue)" stroke-width="1.5"/><ellipse cx="8" cy="8" rx="2.6" ry="6.5" fill="none" stroke="var(--brand-blue)" stroke-width="1.2"/><path d="M1.5 8h13" stroke="var(--brand-blue)" stroke-width="1.2"/></svg>
        </li>
      </ul>
    </div>
  </section>

  <section class="card card-brand">
    <div class="pattern-art" role="img" aria-label="Subtle embossed pattern of overlapping car silhouettes"></div>
    <div class="brand-lockup">
      <span class="brand-dot"></span>
      <div class="brand-text">
        <p class="brand-name">SUMMIT HAUL</p>
        <p class="brand-tagline">The Auto Transport Professionals</p>
      </div>
    </div>
  </section>

</body>
</html>
```